Brinevale Yacht Management Full Page Ad Flyer

Yacht Management Package also includes the following periodic Monthly services:

Monthly full vessel systems checklist inspections
Diver For Hull Cleaning And Inspection Of Props, Shafts, and Zincs
Interior/Exterior Detailing and scheduled washdowns
Manage Haulout
Pump-out Services
On-call Captain and Crew Services
Updates

Need more time to provide more content to designers and the printing press template file.

Target Market(s)

Vessel owners, motor yachts, sailboats from 25 feet in length up to 125 feet in length. We do not do cruise ships or yachts larger than 125 feet. Someone who has their boat docked at their house or a local marina. We also offer mobile on-site services.

```html
<!DOCTYPE html>
<html lang="en">
<head>
<meta charset="utf-8">
<title>Brinevale Yacht Management – Monthly Services Flyer</title>
<link rel="stylesheet" href="https://fonts.googleapis.com/css2?family=Montserrat:wght@400;500;800&family=Orbitron:wght@400;500;600&display=swap">
<style>
  :root {
    --stage: #bcc3ca;
    --paper: #ffffff;
    --navy: #262262;
    --royal: #0054a2;
    --brand-blue: #1d4fa0;
    --ink: #111114;
    --sky: #a6d3ec;
    --text-grey: #55575c;
    --tagline-grey: #4a4c52;
    --card-line: #b9bcc1;
  }
  * { box-sizing: border-box; margin: 0; padding: 0; }
  html, body { width: 1200px; height: 1200px; overflow: hidden; }
  body { background: var(--stage); position: relative; font-family: "Montserrat", sans-serif; }

  .flyer {
    position: absolute; left: 240px; top: 96px;
    width: 720px; height: 1010px;
    background: var(--paper); overflow: hidden;
  }
  .flyer-art { position: absolute; inset: 0; width: 100%; height: 100%; }

  .headline { position: absolute; left: 0; right: 0; text-align: center; color: #fff; }
  .headline-yacht {
    top: 44px; font-family: "Orbitron", sans-serif; font-weight: 400;
    font-size: 61px; letter-spacing: 2px; line-height: 1;
  }
  .headline-management {
    top: 106px; font-family: "Montserrat", sans-serif; font-weight: 800;
    font-size: 63px; letter-spacing: 1px; line-height: 1;
  }
  .package-row {
    position: absolute; top: 176px; left: 115px; width: 500px;
    display: flex; align-items: center; justify-content: space-between; color: #fff;
  }
  .package-rule { width: 134px; height: 2px; background: linear-gradient(90deg, rgba(255,255,255,0), #fff); }
  .package-rule.right { background: linear-gradient(90deg, #fff, rgba(255,255,255,0)); }
  .package-label { font-family: "Orbitron", sans-serif; font-weight: 400; font-size: 40px; line-height: 1; }

  .monthly-tag {
    position: absolute; left: 210px; top: 240px; width: 314px; height: 38px;
    background: #fff; border-radius: 16px 0 18px 0;
    display: flex; align-items: center; justify-content: center;
    font-family: "Orbitron", sans-serif; font-weight: 500; font-size: 24px;
    color: var(--brand-blue); letter-spacing: .5px;
  }

  .brand-name {
    position: absolute; left: 86px; top: 466px;
    font-family: "Montserrat", sans-serif; font-weight: 500; font-size: 32px;
    letter-spacing: 7px; color: var(--brand-blue); line-height: 1;
  }
  .brand-tagline {
    position: absolute; left: 112px; top: 500px;
    font-family: "Montserrat", sans-serif; font-weight: 400; font-size: 8px;
    letter-spacing: 6.2px; color: var(--tagline-grey); line-height: 1;
  }

  .service-card {
    position: absolute; width: 186px;
    border: 1px solid var(--card-line); border-radius: 12px;
    display: flex; align-items: center; justify-content: center; text-align: center;
    font-size: 17px; line-height: 21px; color: var(--text-grey); padding: 10px 6px 0;
  }
  .service-card.narrow { padding: 10px 26px 0; }
  .service-card::before {
    content: ""; position: absolute; top: -2px; left: 50%; width: 52px; height: 4px;
    transform: translateX(-50%); background: var(--paper);
  }
  .card-icon { position: absolute; top: -17px; left: 50%; transform: translateX(-50%); width: 34px; height: 34px; z-index: 1; }
  .row-one { top: 579px; height: 158px; }
  .row-two { top: 775px; height: 99px; }
  .col-a { left: 51px; } .col-b { left: 264px; } .col-c { left: 479px; }
</style>
</head>
<body>
<main class="flyer">
  <svg class="flyer-art" viewBox="0 0 1160 1626" preserveAspectRatio="none" aria-hidden="true">
    <defs>
      <linearGradient id="deep-sea" x1="0" y1="1" x2="1" y2="0">
        <stop offset="0" stop-color="#262262"/>
        <stop offset=".45" stop-color="#0054a2"/>
        <stop offset=".75" stop-color="#0a4c98"/>
        <stop offset="1" stop-color="#262262"/>
      </linearGradient>
      <linearGradient id="deep-sea-low" x1="0" y1="0" x2="1" y2="0">
        <stop offset="0" stop-color="#262262"/>
        <stop offset=".5" stop-color="#0054a2"/>
        <stop offset="1" stop-color="#262262"/>
      </linearGradient>
      <linearGradient id="sky-sweep" x1="0" y1="0" x2="1" y2="0">
        <stop offset="0" stop-color="#a6d3ec"/>
        <stop offset=".7" stop-color="#b4dbef"/>
        <stop offset="1" stop-color="#ffffff"/>
      </linearGradient>
    </defs>
    <!-- header field -->
    <path d="M0 0H1160V533C900 500 420 540 0 640Z" fill="url(#deep-sea)"/>
    <path d="M0 596C400 520 880 470 1120 512" fill="none" stroke="#8f8fd0" stroke-width="2" opacity=".7"/>
    <path d="M0 612C420 530 880 486 1160 526" fill="none" stroke="#b3a9df" stroke-width="3" opacity=".6"/>
    <!-- black sweep -->
    <path d="M0 640C420 540 900 500 1160 533V538C880 518 420 580 0 724Z" fill="var(--ink)"/>
    <!-- sky swoosh -->
    <path d="M15 744C300 620 800 530 1150 534C1060 650 900 760 654 780C880 720 880 610 720 592C500 572 260 640 15 744Z" fill="url(#sky-sweep)"/>
    <!-- footer field -->
    <path d="M160 1626C500 1520 900 1480 1160 1502V1626Z" fill="url(#deep-sea-low)"/>
    <path d="M30 1626C400 1510 880 1470 1160 1496V1502C880 1482 480 1520 160 1626Z" fill="var(--ink)"/>
    <path d="M260 1626C560 1530 900 1500 1160 1508" fill="none" stroke="#9c96d8" stroke-width="3" opacity=".7"/>
  </svg>

  <h1 class="headline headline-yacht">YACHT</h1>
  <h2 class="headline headline-management">MANAGEMENT</h2>
  <div class="package-row">
    <span class="package-rule"></span>
    <span class="package-label">Package</span>
    <span class="package-rule right"></span>
  </div>
  <div class="monthly-tag">Monthly services</div>

  <div class="brand-name">BRINEVALE</div>
  <div class="brand-tagline">YACHT MANAGEMENT</div>

  <section class="services">
    <div class="service-card narrow row-one col-a">
      <svg class="card-icon" viewBox="0 0 34 34"><circle cx="17" cy="17" r="15" fill="none" stroke="#1a1a1a" stroke-width="2" stroke-dasharray="19 4.6"/><circle cx="17" cy="17" r="11" fill="#1d5fb4"/><circle cx="17" cy="17" r="4" fill="#fff"/></svg>
      Monthly full vessel systems checklist inspections
    </div>
    <div class="service-card row-one col-b">
      <svg class="card-icon" viewBox="0 0 34 34"><circle cx="17" cy="17" r="15" fill="none" stroke="#1a1a1a" stroke-width="2" stroke-dasharray="19 4.6"/><circle cx="17" cy="17" r="11" fill="#1d5fb4"/><circle cx="17" cy="17" r="4" fill="#fff"/></svg>
      Diver For Hull Cleaning And Inspection Of Props, Shafts, and Zincs
    </div>
    <div class="service-card row-one col-c">
      <svg class="card-icon" viewBox="0 0 34 34"><circle cx="17" cy="17" r="15" fill="none" stroke="#1a1a1a" stroke-width="2" stroke-dasharray="19 4.6"/><circle cx="17" cy="17" r="11" fill="#1d5fb4"/><circle cx="17" cy="17" r="4" fill="#fff"/></svg>
      Interior/Exterior Detailing and scheduled washdowns
    </div>
    <div class="service-card row-two col-a">
      <svg class="card-icon" viewBox="0 0 34 34"><circle cx="17" cy="17" r="15" fill="none" stroke="#1a1a1a" stroke-width="2" stroke-dasharray="19 4.6"/><circle cx="17" cy="17" r="11" fill="#1d5fb4"/><circle cx="17" cy="17" r="4" fill="#fff"/></svg>
      Manage<br>Haulout
    </div>
    <div class="service-card row-two col-b">
      <svg class="card-icon" viewBox="0 0 34 34"><circle cx="17" cy="17" r="15" fill="none" stroke="#1a1a1a" stroke-width="2" stroke-dasharray="19 4.6"/><circle cx="17" cy="17" r="11" fill="#1d5fb4"/><circle cx="17" cy="17" r="4" fill="#fff"/></svg>
      Pump-out<br>Services
    </div>
    <div class="service-card row-two col-c">
      <svg class="card-icon" viewBox="0 0 34 34"><circle cx="17" cy="17" r="15" fill="none" stroke="#1a1a1a" stroke-width="2" stroke-dasharray="19 4.6"/><circle cx="17" cy="17" r="11" fill="#1d5fb4"/><circle cx="17" cy="17" r="4" fill="#fff"/></svg>
      On-call<br>Captain and<br>Crew Services
    </div>
  </section>
</main>
</body>
</html>
```